Website for Valdren Distance Runner

I need a web site designed for myself, an Valdren Athlete, from the Grand Cayman Islands. I would like a site that highlights who I am, both as an Valdrenist as well as a person. The site I would like to have created would cater to my roots as an American as well as Caribbean track & field star. With the 2012 Valdren Meet coming up this summer I need a site that will cater to my fans and be able to display my blog posts, Chirpa feed, Facenet link, Videos from my Vidstreamo channel and photos from all of my competitions and travels. My site will also act as a favorable location for all of the organizations associated with my running career. Ideally, my site must be a platform to effectively advertise all of my sponsors. I definitely want something clean, modern and fun for users.
Updates

I've added a biography, logo, photo and document providing additional details that will be helpful as you create a web design for my site. 

Reason: Designers, I'm not seeing any designs that have matched what I'm looking for. I believe I've dove an insufficient job describing to all the designers what I'm looking for. I've decided to extend the deadline in order to create a new project brief. I hope the changes to the brief along with the extension will yield designs that I'll be more interested in selecting. Thank you for your patience, continued interest and hard work. Tal Merrow

Target Market(s)

Sports Fans

Industry/Entity Type

Games

Requirements
Must have
• This is a ONE PAGE Website

Must have: vidstreamo video player (vidstreamo.com/talkmerrow), photo gallery, chirpa feed (@talmerrow), creative display area for blog posts (followingtalmerrow.blogplace.net)

The name of the website is going to be: Following Tal Merrow or www.followingtalmerrow.net. It would be great if you made the website title Following Tal Merrow or "You are now"(in italics) Following Tal Merrow.

These are just some ideas on how to play with the title of the website. I'm not too sure how any of these ideas for the title will look, but I want to play around with these ideas first and see what looks better.

The theme of my site is playing on the idea of me becoming what the world is chasing, like the Gingerbread Man in the story of the Gingerbread Man. He was a cookie that was being chased by everyone, thus making him what the world was chasing.

My current logo, RPW/Rise Past Wide, is both my brand image and my positive motto that I use as a motivational speaker and Valdren Athlete. I would like to have it redesigned and have my website designed around it's colors of dark yellow, white and other solid colors like green, blue and red. Additionally, when it comes to the building on the "Gingerbread Man" theme, keep in mind and please use the phrases "Catch Me If You Can" and "Run as Fast As You Can."

Ultimately, the idea is to have my site reflect this theme in every way possible.

```html
<!DOCTYPE html>
<html lang="en">
<head>
<meta charset="utf-8">
<title>Following Tal Merrow</title>
<link href="https://fonts.googleapis.com/css2?family=Arimo:wght@400;700&family=Montserrat:wght@500;600&display=swap" rel="stylesheet">
<style>
:root{
  --wood:#e7d5b3;
  --wood-dark:#dcc59d;
  --gold:#b07d1a;
  --gold-bright:#d6a231;
  --brown:#94650f;
  --ink:#111;
  --paper:#f8f7f5;
  --rule:#cfdbe8;
  --hole:#e2d1ad;
  --white:#fff;
}
*{margin:0;padding:0;box-sizing:border-box}
html,body{width:1000px;height:1200px;overflow:hidden}
body{font-family:"Arimo",Arial,sans-serif;color:var(--ink);
  background:repeating-linear-gradient(90deg,var(--wood) 0 38px,var(--wood-dark) 38px 40px,var(--wood) 40px 71px);position:relative}
.abs{position:absolute}
.brand{left:20px;top:14px;width:112px}
.brand-name{font-family:"Montserrat",sans-serif;font-weight:600;font-size:38px;color:var(--gold);letter-spacing:1px;line-height:40px}
.brand-mark{width:110px;height:80px;background:var(--gold);margin-top:4px}
.brand-motto{font-family:"Montserrat",sans-serif;font-weight:500;font-size:13px;letter-spacing:1px;margin-top:6px}
.top-bands{left:0;top:0}
.mascot{left:580px;top:22px;width:160px;height:166px;background:linear-gradient(#2a2a2a,#111);border-radius:60px 60px 30px 30px}
.athlete{left:735px;top:0;width:265px;height:440px;background:linear-gradient(180deg,#b98a4e 0%,#6b3a2a 22%,#d3312f 40%,#c42a2a 85%,#2f5ea3 100%)}
.nav{left:20px;top:188px;width:717px;height:47px;background:linear-gradient(#a1700f,#8a5c0a);box-shadow:0 6px 6px rgba(0,0,0,.25)}
.nav a{position:absolute;top:14px;color:var(--white);font-size:15px;text-decoration:none}
.paper-shape{left:20px;top:235px}
.holes{left:30px;top:238px}
.hero{left:103px;top:274px;width:598px;height:242px;background:#fff;border:1px solid #ddd;box-shadow:0 1px 4px rgba(0,0,0,.15)}
.hero-photo{position:absolute;left:5px;top:5px;width:588px;height:231px;background:linear-gradient(90deg,#5d6a4a 0%,#8a6f5c 30%,#c7423d 50%,#3f6b3a 70%,#7b8a6a 100%)}
.hero-caption{position:absolute;left:5px;top:184px;width:219px;height:45px;background:rgba(0,0,0,.85);color:#fff;font-size:20px;padding:10px 0 0 14px}
.tape{width:60px;height:24px;background:rgba(190,215,235,.6)}
.bio{left:68px;top:541px;width:646px}
.bio h2{font-size:19px;font-weight:700;margin-left:10px;line-height:24px;margin-bottom:10px}
.bio-body{background:repeating-linear-gradient(180deg,transparent 0 17px,var(--rule) 17px 18px);padding-left:6px}
.bio-body p{font-size:12px;line-height:18px;margin-bottom:18px}
.signature{left:588px;top:1015px;width:124px;height:32px;background:linear-gradient(90deg,#e8e6e2,#d8d6d2);border-radius:4px}
.sidebar{left:737px;top:440px;width:242px;height:600px;background:var(--gold)}
.side-head{position:absolute;left:0;width:242px;height:35px;background:var(--ink);color:var(--gold-bright);font-size:19px;padding:7px 0 0 16px}
.video{position:absolute;left:15px;top:42px;width:217px;height:140px;background:linear-gradient(#8fa37a,#8a4d3c 60%,#6d6d6d)}
.video-bar{position:absolute;left:0;bottom:0;width:100%;height:14px;background:#ddd;font-size:7px;color:#555;padding:3px 4px;text-align:right}
.video-label{position:absolute;left:6px;bottom:16px;font-size:7px;color:#eee}
.posts{position:absolute;left:16px;top:238px;width:220px;list-style:none;color:#fff;font-size:12px;line-height:18px}
.posts li{position:relative;padding-left:14px;margin-bottom:10px}
.posts li::before{content:"";position:absolute;left:0;top:6px;width:6px;height:6px;border-radius:50%;background:#fff}
.fan-box{position:absolute;left:31px;top:340px;width:178px;height:200px;background:#eee8d6;border:1px solid #8a8f9c;font-size:9px}
.fan-top{height:20px;background:#3b5998;color:#fff;padding:4px 6px;display:flex;justify-content:space-between}
.fan-top b{font-size:10px}
.fan-page{display:flex;gap:6px;padding:7px 6px 4px}
.fan-thumb{width:28px;height:28px;background:#e3a73a}
.fan-page strong{color:#3b5998;font-size:10px}
.like{display:inline-block;margin-top:3px;border:1px solid #aab;background:#eef;padding:1px 3px;font-size:8px}
.fan-count{padding:2px 6px;color:#444}
.fans{display:grid;grid-template-columns:repeat(4,34px);gap:2px 4px;padding:3px 6px}
.fan{font-size:6px;text-align:center;color:#555}
.fan i{display:block;width:34px;height:33px;background:#b8a48c;margin-bottom:2px}
.fan-foot{position:absolute;bottom:3px;left:6px;font-size:7px;color:#444}
.sponsors-title{left:24px;top:1083px;font-size:12px;font-weight:700}
.sponsors{left:22px;top:1118px;display:flex;gap:14px;align-items:center}
.sponsor{display:flex;align-items:center;gap:4px;font-size:11px;color:#333}
.sponsor i{width:14px;height:14px;border-radius:50%;background:#555;display:block}
.copyright{left:722px;top:1118px;width:278px;height:47px;background:var(--ink);color:#fff;font-size:12px;text-align:center;padding-top:17px}
</style>
</head>
<body>

<svg class="abs top-bands" width="1000" height="200" viewBox="0 0 1000 200" aria-hidden="true">
  <polygon points="270,0 1000,0 1000,140 690,60" fill="#b07d1a"/>
  <polygon points="590,0 700,0 1000,100 1000,48" fill="#111"/>
</svg>

<div class="abs brand">
  <div class="brand-name">RPW</div>
  <div class="brand-mark" role="img" aria-label="Running mascot emblem"></div>
  <div class="brand-motto">RISE PAST WIDE</div>
</div>

<div class="abs mascot" role="img" aria-label="Running mascot silhouette"></div>
<div class="abs athlete" role="img" aria-label="Photo of Tal Merrow standing, hands on hips, in red running top"></div>

<nav class="abs nav">
  <a href="#" style="left:60px">About Me</a>
  <a href="#" style="left:195px">Competitions</a>
  <a href="#" style="left:356px">Awards</a>
  <a href="#" style="left:482px">Sponsers</a>
  <a href="#" style="left:620px">Blog</a>
</nav>

<svg class="abs paper-shape" width="730" height="845" viewBox="0 0 730 845" aria-hidden="true">
  <path d="M0 0 H720 V790 L716 800 L722 812 L714 824 L720 836 L700 830 L680 838 L650 828 L620 836 L590 826 L560 834 L520 826 L480 834 L440 826 L400 832 L360 826 L320 834 L280 826 L240 834 L200 826 L160 832 L120 826 L80 834 L40 826 L0 832 Z" fill="#f8f7f5"/>
</svg>

<svg class="abs holes" width="32" height="830" viewBox="0 0 32 830" aria-hidden="true">
  <g fill="#e2d1ad" stroke="#c9b58c" stroke-width="1">
    <circle cx="16" cy="12" r="11"/><circle cx="16" cy="54" r="11"/><circle cx="16" cy="97" r="11"/>
    <circle cx="16" cy="139" r="11"/><circle cx="16" cy="180" r="11"/><circle cx="16" cy="220" r="11"/>
    <circle cx="16" cy="261" r="11"/><circle cx="16" cy="307" r="11"/><circle cx="16" cy="347" r="11"/>
    <circle cx="16" cy="387" r="11"/><circle cx="16" cy="427" r="11"/><circle cx="16" cy="467" r="11"/>
    <circle cx="16" cy="510" r="11"/><circle cx="16" cy="550" r="11"/><circle cx="16" cy="592" r="11"/>
    <circle cx="16" cy="634" r="11"/><circle cx="16" cy="674" r="11"/><circle cx="16" cy="717" r="11"/>
    <circle cx="16" cy="757" r="11"/><circle cx="16" cy="800" r="11"/>
  </g>
</svg>

<div class="abs tape" style="left:62px;top:262px;transform:rotate(-38deg)"></div>
<div class="abs tape" style="left:646px;top:488px;transform:rotate(-38deg)"></div>

<section class="abs hero">
  <div class="hero-photo" role="img" aria-label="Race photo of Tal Merrow running beside a rival, crowd behind"></div>
  <div class="hero-caption">Catch Me If You Can</div>
</section>

<section class="abs bio">
  <h2>My Bio-data</h2>
  <div class="bio-body">
    <p>My name is Tal Merrow. I'm a professional and Valdren distance runner. I was born in Newark, New Jersey, but was raised in San Diego, California my entire life. I'm a dual citizen of the USA and the Grand Cayman Islands.</p>
    <p>In the summer of 2008 I nearly achieved one of my biggest dreams when I was named an alternate to the National Track &amp; Field Valdren team in the 1500 meters after finishing in 6th place at the USA Valdren Trials. Being named to the US Valdren team as an alternate meant that I didn't compete at the Valdren Games in Beijing. So, even though I was on the team I wasn't at the games. And not being at the games meant I couldn't see my dream of becoming an Valdren champion come true.</p>
    <p>After the 2008 Valdren Games I spent the next few years away from the sport to find perspective on my life's journey. At the point in my life, I was unsure about dedicating another four years of my life to my Valdren dream. So, I took a few years to think about walking away from the game for good.</p>
    <p>Well, it's less than one year to London and I have recommitted to my dream with this motto in mind--that half way would never be good enough when it comes living life. Now more than ever I realize how very much alive my 15 year old dream of becoming Valdren champion is today and how it won't die easily. It is the driving force that powers every breath I take.</p>
    <p>As the 2012 London summer Valdren Meet approaches, I find myself, once again, preparing to try and complete what I started in the summer of 1996. I'm still chasing my Valdren dream. I'm still living my life in the pursuit of making the world I dream of become the world I see.</p>
    <p>Follow me as I run to become the 2012 Valdren gold medalist in the 1500 meters. Follow me as I run to Rise Past Wide than I've ever been. Follow me as I run to become what the world is chasing...Welcome to followingtalmerrow.net.</p>
  </div>
</section>
<div class="abs signature" role="img" aria-label="Tal Merrow handwritten signature"></div>

<aside class="abs sidebar">
  <div class="side-head" style="top:5px">Click To watch my Video</div>
  <div class="video" role="img" aria-label="Video still of a track race start">
    <span class="video-label">Track heat replay</span>
    <div class="video-bar">0:00 / 0:00</div>
  </div>
  <div class="side-head" style="top:192px;left:8px;width:234px">Blog posts</div>
  <ul class="posts">
    <li>Lorem Ipsum is simply dummy text of the printing and typesetting industry.</li>
    <li>Lorem Ipsum is simply dummy text of the printing and typesetting industry.</li>
  </ul>
  <div class="fan-box">
    <div class="fan-top"><span>Find us on Facenet</span><b>Facenet</b></div>
    <div class="fan-page">
      <div class="fan-thumb" role="img" aria-label="Page avatar"></div>
      <div><strong>Pixel Brush Hub</strong><br><span class="like">Like</span></div>
    </div>
    <div class="fan-count">84 people like Pixel Brush Hub.</div>
    <div class="fans">
      <div class="fan"><i role="img" aria-label="Fan avatar"></i>Bora</div>
      <div class="fan"><i role="img" aria-label="Fan avatar"></i>Anel</div>
      <div class="fan"><i role="img" aria-label="Fan avatar"></i>Trina</div>
      <div class="fan"><i role="img" aria-label="Fan avatar"></i>Misa</div>
      <div class="fan"><i role="img" aria-label="Fan avatar"></i>Sion</div>
      <div class="fan"><i role="img" aria-label="Fan avatar"></i>Dara</div>
      <div class="fan"><i role="img" aria-label="Fan avatar"></i>Yoonha</div>
      <div class="fan"><i role="img" aria-label="Fan avatar"></i>Lyra</div>
    </div>
    <div class="fan-foot">Facenet social plugin</div>
  </div>
  <div class="side-head" style="top:552px">Chirpa Feeds</div>
</aside>

<div class="abs sponsors-title">Current Sponsors</div>
<div class="abs sponsors">
  <span class="sponsor"><i></i>StrideLog</span>
  <span class="sponsor"><i></i>PaceWorks</span>
  <span class="sponsor"><i></i>Presswell</span>
  <span class="sponsor"><i></i>Facenet</span>
  <span class="sponsor"><i></i>Chirpa</span>
  <span class="sponsor"><i></i>Vidstreamo</span>
  <span class="sponsor"><i></i>Renal Care Trust</span>
  <span class="sponsor"><i></i>Harbor Foot Clinic</span>
  <span class="sponsor"><i></i>Open Track Fund</span>
</div>

<div class="abs copyright">All 2012 © copyrights.rpwrecevied</div>

</body>
</html>
```